Business Card Design needed for logo design project

We need a business card design for a construction parts business.

We would like our main company logo on the front of the card and have our other company website logo on the rear of the card.

Both logos will be attached.

Front of card
Logo is KRV
Can we also have the wording "Construction Equipment Parts Specialists"
Main details to include:

Address:
Telephone:
Mobile:
Email:
Website:

Rear of card.

Logo is gearlodgehub.com.au (we would like this logo taking up the most of the rear)
Also we want under gearlodgehub.com.au the following wording "Parts Sourced For You From Across The Globe"
Updates

Please see new update for our design

Target Market(s)

Construction Industry.
Earthmoving Equipment owners.

Industry/Entity Type

Construction

Font styles to use
Sans Serif

Requirements
Must have
• Easy to read.
Clean and smart.
Should not have
• Should not have any colours other than the colours of our logos.

```html
<!DOCTYPE html>
<html lang="en">
<head>
<meta charset="utf-8">
<title>KRV Business Card</title>
<link rel="stylesheet" href="https://fonts.googleapis.com/css2?family=Roboto+Condensed:wght@400;700&display=swap">
<style>
  :root {
    --navy: #1e3a52;
    --teal: #2e8aa5;
    --white: #ffffff;
    --backdrop: #e9e6e1;
    --ink-soft: #dfe8ee;
  }
  * { margin: 0; padding: 0; box-sizing: border-box; }
  html, body {
    width: 1200px; height: 1023px; overflow: hidden;
    background: var(--backdrop);
    font-family: "Roboto Condensed", Arial, sans-serif;
  }
  .card {
    position: absolute;
    width: 640px; height: 391px;
    background: var(--white);
    box-shadow: 0 6px 18px rgba(0,0,0,.18);
    overflow: hidden;
  }
  .card--front { left: 60px; top: 80px; }
  .card--back { left: 500px; top: 552px; }

  .front-shapes { position: absolute; inset: 0; }

  .brand { position: absolute; left: 44px; top: 112px; color: var(--navy); }
  .brand__name { font-size: 104px; font-weight: 700; line-height: 1; letter-spacing: 2px; }
  .brand__tagline { font-size: 19px; font-weight: 400; line-height: 1.15; text-align: center; margin-top: 8px; }

  .contact {
    position: absolute; right: 30px; top: 28px;
    color: var(--white); text-align: right; font-size: 17px; line-height: 1.3;
  }
  .contact__address { margin-bottom: 26px; }
  .contact__row { display: flex; justify-content: flex-end; align-items: center; gap: 8px; }
  .contact__icon { width: 14px; height: 14px; flex: none; }

  .person { position: absolute; left: 345px; top: 296px; }
  .person__name { color: var(--teal); font-size: 25px; font-weight: 400; }
  .person__role { color: var(--white); font-size: 19px; margin-top: 2px; }

  .site-mark {
    position: absolute; left: 58px; top: 158px;
    display: flex; align-items: center; gap: 12px;
  }
  .site-mark__name {
    color: var(--navy); font-size: 47px; font-weight: 700; letter-spacing: 0.5px;
  }
  .site-mark__dot { width: 46px; height: 46px; border-radius: 50%; background: var(--teal); }
  .site-tagline {
    position: absolute; left: 58px; top: 216px;
    color: var(--teal); font-size: 21px; font-weight: 400;
  }
</style>
</head>
<body>

<section class="card card--front" aria-label="Business card front">
  <svg class="front-shapes" viewBox="0 0 640 391" width="640" height="391" aria-hidden="true">
    <path fill="var(--teal)" d="M198,391 C272,312 318,210 352,118 C372,66 400,30 440,8 C408,38 388,80 370,128 C336,222 292,320 236,391 Z"/>
    <path fill="var(--navy)" d="M248,391 C310,310 348,210 380,126 C406,60 450,18 560,0 L640,0 L640,391 Z"/>
    <path fill="none" stroke="var(--white)" stroke-width="5" d="M452,0 C410,26 388,72 372,120"/>
  </svg>

  <div class="brand">
    <div class="brand__name">KRV</div>
    <div class="brand__tagline">Construction Equipment Parts<br>Specialists</div>
  </div>

  <div class="contact">
    <div class="contact__address">Suite 88 Harbour Rd.,<br>Level 2 Sydney,<br>NSW 20000</div>
    <div class="contact__row"><span>02-555-0142</span>
      <svg class="contact__icon" viewBox="0 0 14 14"><path fill="var(--ink-soft)" d="M3 1l2.5 2.5-1.5 1.5c.8 1.8 2.2 3.2 4 4l1.5-1.5L12 10l-1.5 2.5C6 12 2 8 1.5 3.5Z"/></svg></div>
    <div class="contact__row"><span>02-555-0198</span>
      <svg class="contact__icon" viewBox="0 0 14 14"><rect x="3.5" y="1" width="7" height="12" rx="1.2" fill="none" stroke="var(--ink-soft)" stroke-width="1.4"/></svg></div>
    <div class="contact__row"><span>info@krv.com.au</span>
      <svg class="contact__icon" viewBox="0 0 14 14"><rect x="1" y="3" width="12" height="8.5" fill="var(--ink-soft)"/><path d="M1 3l6 5 6-5" fill="none" stroke="var(--navy)" stroke-width="1.2"/></svg></div>
    <div class="contact__row"><span>www.gearlodgehub.com.au</span>
      <svg class="contact__icon" viewBox="0 0 14 14"><circle cx="7" cy="7" r="5.8" fill="none" stroke="var(--ink-soft)" stroke-width="1.4"/><path d="M1.2 7h11.6M7 1.2c-2.5 3-2.5 8.6 0 11.6M7 1.2c2.5 3 2.5 8.6 0 11.6" fill="none" stroke="var(--ink-soft)" stroke-width="1"/></svg></div>
  </div>

  <div class="person">
    <div class="person__name">Daniel Harwood</div>
    <div class="person__role">General Manager</div>
  </div>
</section>

<section class="card card--back" aria-label="Business card back">
  <div class="site-mark">
    <span class="site-mark__name">GEARLODGEHUB.COM.AU</span>
    <span class="site-mark__dot"></span>
  </div>
  <div class="site-tagline">Parts Sourced For You From Across The Globe</div>
</section>

</body>
</html>
```